Brindel Clear Springs needs a new business card design (we produce and sell pure bottled water)

We need a clean modern design for our new business cards, We have an existing logo which ultimately cannot be changed, however it could be slighty improved and the colours adjusted. We have this existing logo on all of our bottles, vehicles etc.

Our company slogan is "Pure down to the last drop".
Along with our relevant company information
(Address, phone, website email etc) we will only be using names and not putting position titles for flexibilty.

We are looking for a clean, minimalist modern design.

You can view our website (if need of an update also!) to see our business.

Industry/Entity Type

Business

Contact Information for Business Card

Staff Name : XXXXXX XXXXXX
Address : 8/41 Tallowood St
Marwick Flats QLD 4172
Staff Mobile Number : 04XX XXX XXX
Office Phone Number : 07 3918 4520
Staff Email Address : XXXX@brindelclearsprings.com.au
Website : www.brindelclearsprings.com.au

Font styles to use
Sans Serif

Colors
cee9f5
33a6d7
0492cd
0455a3
3276b5
85abd2
cedeed

Requirements
Must have
• The ability to edit and change the staff members details as we will need to edit for each respective staff member (7 in total)

```html
<!DOCTYPE html>
<html lang="en">
<head>
<meta charset="utf-8">
<title>Brindel Clear Springs – Business Card</title>
<link href="https://fonts.googleapis.com/css2?family=Arimo:wght@700&display=swap" rel="stylesheet">
<style>
  :root {
    --canvas: #e9ebec;
    --card: #ffffff;
    --brand-navy: #2b2a8c;
    --contact-blue: #1f5fae;
    --water-light: #cee9f5;
    --water-mid: #85abd2;
    --water-deep: #33a6d7;
    --water-dark: #0455a3;
  }
  * { box-sizing: border-box; margin: 0; padding: 0; }
  html, body { width: 1200px; height: 1199px; overflow: hidden; }
  body {
    background: var(--canvas);
    font-family: "Arimo", Arial, sans-serif;
    font-weight: 700;
    position: relative;
  }
  .card {
    position: absolute;
    top: 436px;
    width: 545px;
    height: 327px;
    background: var(--card);
    overflow: hidden;
    box-shadow: 0 2px 10px rgba(0,0,0,.12);
  }
  .card--front { left: 40px; }
  .card--back { left: 615px; }

  .brand {
    position: absolute;
    display: flex;
    align-items: center;
    gap: 10px;
    color: var(--brand-navy);
    line-height: 1;
  }
  .brand__dot {
    width: 26px; height: 26px;
    border-radius: 50%;
    background: var(--brand-navy);
    flex: none;
  }
  .brand__name { display: flex; flex-direction: column; }
  .brand__line1 { letter-spacing: .5px; }
  .card--front .brand { left: 62px; top: 170px; }
  .card--front .brand__line1 { font-size: 36px; }
  .card--front .brand__line2 { font-size: 19px; margin-top: 4px; }
  .card--back .brand { left: 50px; top: 158px; gap: 8px; }
  .card--back .brand__dot { width: 18px; height: 18px; }
  .card--back .brand__line1 { font-size: 22px; }
  .card--back .brand__line2 { font-size: 12px; margin-top: 3px; }

  .water { position: absolute; }
  .water--front-band {
    left: 0; right: 0; bottom: 0; height: 52px;
    background: linear-gradient(180deg, var(--water-light) 0%, var(--water-mid) 45%, var(--water-deep) 100%);
  }
  .water--front-splash {
    left: 245px; bottom: 40px; width: 250px; height: 110px;
    background: radial-gradient(ellipse at 55% 90%, var(--water-mid) 0%, var(--water-light) 50%, rgba(255,255,255,0) 75%);
  }
  .water--back-band {
    left: 0; right: 0; top: 0; height: 44px;
    background: linear-gradient(0deg, var(--water-light) 0%, var(--water-mid) 50%, var(--water-deep) 100%);
  }
  .water--back-splash {
    left: 230px; top: 30px; width: 270px; height: 115px;
    background: radial-gradient(ellipse at 50% 15%, var(--water-mid) 0%, var(--water-light) 48%, rgba(255,255,255,0) 75%);
  }

  .contact {
    position: absolute;
    left: 234px;
    top: 147px;
    color: var(--contact-blue);
  }
  .contact__name { font-size: 22px; letter-spacing: 1px; margin-bottom: 8px; }
  .contact__list { list-style: none; }
  .contact__item {
    display: flex;
    align-items: flex-start;
    gap: 9px;
    font-size: 13.5px;
    line-height: 1.05;
    margin-bottom: 12px;
  }
  .contact__icon { width: 15px; height: 15px; flex: none; fill: var(--contact-blue); }
</style>
</head>
<body>

<section class="card card--front" aria-label="Card front">
  <div class="water water--front-splash" role="img" aria-label="Splashing water and bubbles"></div>
  <div class="water water--front-band" role="img" aria-label="Clear blue water surface"></div>
  <div class="brand">
    <span class="brand__dot"></span>
    <span class="brand__name">
      <span class="brand__line1">BRINDEL</span>
      <span class="brand__line2">CLEAR SPRINGS</span>
    </span>
  </div>
</section>

<section class="card card--back" aria-label="Card back">
  <div class="water water--back-band" role="img" aria-label="Clear blue water surface"></div>
  <div class="water water--back-splash" role="img" aria-label="Falling water bubbles"></div>
  <div class="brand">
    <span class="brand__dot"></span>
    <span class="brand__name">
      <span class="brand__line1">BRINDEL</span>
      <span class="brand__line2">CLEAR SPRINGS</span>
    </span>
  </div>
  <div class="contact">
    <p class="contact__name">MARTEN</p>
    <ul class="contact__list">
      <li class="contact__item">
        <svg class="contact__icon" viewBox="0 0 16 16" aria-hidden="true"><rect x="4" y="1" width="9" height="14" rx="1.5"/><rect x="5.5" y="3" width="6" height="8" fill="#fff"/></svg>
        <span>07 3918 4520</span>
      </li>
      <li class="contact__item">
        <svg class="contact__icon" viewBox="0 0 16 16" aria-hidden="true"><rect x="1" y="3" width="14" height="10"/><path d="M1.5 3.5 8 9l6.5-5.5" fill="none" stroke="#fff" stroke-width="1.4"/></svg>
        <span>brindelclearsprings@gmail.com</span>
      </li>
      <li class="contact__item">
        <svg class="contact__icon" viewBox="0 0 16 16" aria-hidden="true" fill="none" stroke="#1f5fae" stroke-width="1.1" style="fill:none"><circle cx="8" cy="8" r="6.5"/><ellipse cx="8" cy="8" rx="3" ry="6.5"/><path d="M1.5 8h13M2.5 4.8h11M2.5 11.2h11"/></svg>
        <span>www.brindelclearsprings.com.au</span>
      </li>
      <li class="contact__item">
        <svg class="contact__icon" viewBox="0 0 16 16" aria-hidden="true"><path d="M8 1.5 1 8h2v6.5h4v-4h2v4h4V8h2z"/></svg>
        <span>8/41 Tallowood St Marwick<br>Flats QLD 4172</span>
      </li>
    </ul>
  </div>
</section>

</body>
</html>
```